Harbor Oncology Partners Patient Referral Card

We need a 3.75" wide by 8.25" long patient referral card that a physician will fill out to refer their patient to Harbor Oncology Partners. The front of the card will have our logo on top, followed by contact information, a map that shows the office location and then there will be descriptive text at the bottom. On the back side, there will be a headshot photo with a brief bio of Dr. Marcus Whitfield. The address for the office is: 4175 N. Larchmont, Puyallup, WA 98461. The office phone number is 253.400.7218 and the website address is: harboroncologyhub.com

Target Market(s)

Physicians and medical staff

Font styles to use
Serif

Colors
34a7d8
33b8a4
9bcb3c

Requirements
Must have
• A map of the office location and two text boxes for descriptive language about services, and a photo and bio of Dr. Marcus Whitfield
Nice to have
• Clean and distinct design that is eye catching
Should not have
• Flowery or bold colors that distract from the content and purpose of the card

```html
<!DOCTYPE html>
<html lang="en">
<head>
<meta charset="utf-8">
<title>Harbor Oncology Partners – Patient Referral Card</title>
<link rel="stylesheet" href="https://fonts.googleapis.com/css2?family=Roboto:wght@300;400;500;700&family=Roboto+Condensed:wght@400;700&display=swap">
<style>
  :root{
    --teal:#28b3c0;
    --teal-deep:#22a9b6;
    --green:#5cb848;
    --ink:#111111;
    --black:#0b0b0b;
    --white:#ffffff;
    --map:#e6eaec;
    --stage:#dcdedf;
  }
  *{box-sizing:border-box;margin:0;padding:0}
  html,body{width:1200px;height:1200px;overflow:hidden}
  body{background:var(--stage);position:relative;font-family:"Roboto",sans-serif}

  .card{position:absolute;width:427px;height:939px;overflow:hidden;box-shadow:8px 14px 26px rgba(0,0,0,.28)}

  /* ---------- front ---------- */
  .card--front{left:107px;top:101px;background:linear-gradient(180deg,var(--white) 0%,var(--white) 56%,#cfeef1 68%,var(--teal) 100%)}
  .brand{position:absolute;left:88px;top:50px;display:flex;align-items:center;gap:16px}
  .brand__dot{width:42px;height:42px;border-radius:50%;background:var(--teal);flex:none}
  .brand__name{font-family:"Roboto",sans-serif;font-weight:300;color:var(--teal);font-size:27px;line-height:32px;letter-spacing:2px;border-left:2px solid var(--teal);padding-left:12px}
  .front__tagline{position:absolute;left:0;width:427px;top:168px;text-align:center;font-size:11px;letter-spacing:6.5px;color:#333;padding-left:20px}
  .front__phone{position:absolute;left:0;width:427px;top:185px;text-align:center;font-weight:700;font-size:35px;color:var(--ink);padding-left:6px}
  .front__web{position:absolute;left:0;width:427px;top:227px;text-align:center;font-weight:500;font-size:18px;color:var(--ink);padding-left:6px}
  .front__swoosh{position:absolute;left:0;top:222px}
  .map{position:absolute;left:10px;top:297px;width:415px;height:226px;background:var(--map)}
  .map__pin{position:absolute;left:32px;top:52px}
  .map__label{position:absolute;left:68px;top:64px;background:#22b04b;border-radius:20px;padding:3px 14px 4px 18px;font-family:"Roboto Condensed",sans-serif;color:#111;line-height:1.1}
  .map__label b{display:block;font-weight:400;font-size:19px}
  .map__label span{font-size:15px}
  .refer__title{position:absolute;left:0;width:427px;top:548px;text-align:center;font-family:"Roboto Condensed",sans-serif;font-weight:700;font-size:50px;color:var(--teal);letter-spacing:.5px}
  .refer__field{position:absolute;left:43px;width:347px;border-bottom:2px solid var(--white);font-family:"Roboto Condensed",sans-serif;font-size:20px;color:#333;padding-bottom:3px}

  /* ---------- back ---------- */
  .card--back{left:623px;top:187px;background:var(--black)}
  .back__photo{position:absolute;left:0;top:0}
  .back__name{position:absolute;left:0;width:427px;top:530px;text-align:center;color:var(--teal);font-size:36px;font-weight:400}
  .back__name small{font-size:22px}
  .back__role{position:absolute;left:0;width:427px;top:571px;text-align:center;color:var(--white);font-size:22px;font-weight:300}
  .back__copy{position:absolute;left:20px;width:387px;text-align:center;font-family:"Roboto Condensed",sans-serif;color:var(--white);font-size:19px;line-height:23px}
  .back__footer{position:absolute;left:0;top:809px;width:427px;height:101px}
  .back__tab{position:absolute;left:0;top:0;width:33px;height:101px;background:var(--teal)}
  .back__brand{position:absolute;left:46px;top:8px;display:flex;align-items:center;gap:10px}
  .back__brand .brand__dot{width:30px;height:30px}
  .back__brand .brand__name{font-size:21px;line-height:26px;letter-spacing:1.5px;padding-left:8px}
  .back__tagline{position:absolute;left:46px;top:110px;font-size:8px;letter-spacing:4.6px;color:#aaa}
  .back__contact{position:absolute;left:234px;top:0;width:193px;height:101px;background:var(--teal);padding:10px 0 0 13px;color:var(--ink)}
  .back__contact .phone{font-weight:700;font-size:24px}
  .back__contact .addr{font-size:12px;line-height:15px;margin-top:5px}
  .back__contact .web{font-weight:700;font-size:12.5px;margin-top:12px}
</style>
</head>
<body>

<section class="card card--front" aria-label="Referral card front">
  <div class="brand">
    <span class="brand__dot"></span>
    <div class="brand__name">Harbor<br>Oncology<br>Partners</div>
  </div>
  <div class="front__tagline">RADIATION ONCOLOGY</div>
  <div class="front__phone">253-400-7218</div>
  <div class="front__web">www.harboroncologyhub.com</div>
  <svg class="front__swoosh" width="427" height="80" viewBox="0 0 427 80">
    <path d="M0 62 C160 78 330 52 427 5 L427 18 C330 62 160 86 0 66 Z" fill="var(--teal)"/>
    <path d="M10 66 C170 84 330 64 427 22 L427 38 C330 74 170 90 10 66 Z" fill="var(--green)"/>
  </svg>

  <div class="map" role="img" aria-label="Street map showing the office location">
    <svg class="map__pin" width="30" height="46" viewBox="0 0 30 46">
      <path d="M15 0 C6.7 0 0 6.7 0 15 C0 26 15 46 15 46 C15 46 30 26 30 15 C30 6.7 23.3 0 15 0 Z" fill="#e53b2e"/>
      <circle cx="15" cy="14" r="5" fill="#a4231a"/>
    </svg>
    <div class="map__label"><b>4175 N. Larchmont</b><span>Puyallup, WA 98461.</span></div>
  </div>

  <div class="refer__title">REFER A FRIEND</div>
  <div class="refer__field" style="top:626px">YOUR NAME :</div>
  <div class="refer__field" style="top:684px">FRIEND</div>
  <div class="refer__field" style="top:737px">PHONE</div>
  <div class="refer__field" style="top:791px">FRIEND</div>
  <div class="refer__field" style="top:845px">PHONE</div>
</section>

<section class="card card--back" aria-label="Referral card back">
  <svg class="back__photo" width="427" height="510" viewBox="0 0 427 510" role="img" aria-label="Headshot photo of Dr. Marcus Whitfield in a dark suit">
    <defs>
      <linearGradient id="photoTone" x1="0" y1="0" x2="0" y2="1">
        <stop offset="0" stop-color="#e7e8e6"/>
        <stop offset=".55" stop-color="#b9b6b2"/>
        <stop offset="1" stop-color="#2b2d33"/>
      </linearGradient>
    </defs>
    <path d="M0 0 H427 V448 C330 490 180 505 0 505 Z" fill="url(#photoTone)"/>
    <path d="M0 505 C180 505 330 490 427 448 L427 462 C330 500 180 510 0 510 Z" fill="var(--teal)"/>
  </svg>

  <div class="back__name">Dr. Marcus Whitfield, <small>MD PhD</small></div>
  <div class="back__role">Radiation Oncology</div>
  <p class="back__copy" style="top:622px">The leading cancer care treatment center in the South Puget Sound Region of Washington State.</p>
  <p class="back__copy" style="top:713px">We customize a treatment plan for your unique diagnosis.</p>

  <div class="back__footer">
    <div class="back__tab"></div>
    <div class="back__brand">
      <span class="brand__dot"></span>
      <div class="brand__name">Harbor<br>Oncology<br>Partners</div>
    </div>
    <div class="back__contact">
      <div class="phone">253-400-7218</div>
      <div class="addr">4175 N. Larchmont, Puyallup,<br>WA 98461.</div>
      <div class="web">www.harboroncologyhub.com</div>
    </div>
  </div>
  <div class="back__tagline" style="top:921px">RADIATION ONCOLOGY</div>
</section>

</body>
</html>
```